Sarood Tradeline Web Design

We need Simple but very Elegant Website for Our Middle East Company based in Kuwait, We are not good in describing design but we need simple but elegant and responsive to attract new market and to enable us competing in business

Industry/Entity Type

It Company

```html
<!DOCTYPE html>
<html lang="en">
<head>
<meta charset="utf-8">
<title>Logo Here</title>
<link rel="stylesheet" href="https://fonts.googleapis.com/css2?family=Poppins:wght@300;400;500;600;700&family=Archivo+Black&display=swap">
<style>
:root{
  --ink:#0b0b0c;
  --white:#ffffff;
  --accent:#f4b86a;
  --accent-deep:#f0a23c;
  --gold:#f5b945;
  --charcoal:#323436;
  --field:#3a3b3d;
  --hex:#6d6d6d;
  --hex-text:#3c3c3c;
  --body-text:#3d3d3d;
  --muted:#cfcfcf;
}
*{margin:0;padding:0;box-sizing:border-box}
html,body{width:1200px;height:3416px;overflow:hidden}
body{position:relative;font-family:"Poppins",Arial,sans-serif;color:var(--white);background:var(--white)}
.abs{position:absolute}

/* hero */
.hero{position:absolute;left:0;top:0;width:1200px;height:710px;overflow:hidden}
.hero-photo{position:absolute;inset:0;background:linear-gradient(180deg,#3d4a66 0%,#5b6172 30%,#6f6c66 55%,#4b4a3d 78%,#2b2a24 100%)}
.hero-shade{position:absolute;inset:0;background:rgba(10,12,18,.45)}
.hero-topband{position:absolute;left:0;top:0;width:1200px;height:84px;background:rgba(0,0,0,.35)}
.hero-rail{position:absolute;left:1116px;top:0;width:84px;height:710px;background:rgba(0,0,0,.72)}
.hero-rail-line{position:absolute;left:1160px;top:114px;width:2px;height:104px;background:var(--white)}
.social{position:absolute;left:1148px;width:25px;height:25px;border-radius:50%;background:var(--white);opacity:.85}
.brand-box{position:absolute;left:0;top:0;width:235px;height:312px;background:var(--ink);padding:34px 0 0 42px}
.brand-box .name{font-size:50px;line-height:64px;font-weight:300;letter-spacing:1px}
.brand-box .count{position:absolute;left:148px;top:154px;font-size:22px;font-weight:300}
.brand-box .index{position:absolute;left:50px;top:178px;font-size:80px;font-weight:300;color:var(--gold);line-height:1}
.main-nav{position:absolute;top:0;left:0;width:1200px;height:76px;font-size:15px;font-weight:400;letter-spacing:.3px}
.main-nav span,.main-nav a{position:absolute;top:27px;color:var(--white);text-decoration:none;white-space:nowrap}
.hero-title{position:absolute;right:232px;top:244px;font-size:53px;font-weight:500;letter-spacing:1px}
.hero-copy{position:absolute;right:232px;top:352px;width:520px;text-align:right;font-size:18px;line-height:26px;font-weight:300}
.btn{position:absolute;display:flex;align-items:center;justify-content:center;background:var(--accent);color:var(--white);font-size:16px;font-weight:500}
.slide-dots{position:absolute;left:0;top:496px;width:62px;height:146px;background:rgba(0,0,0,.7)}
.slide-dots span{position:absolute;left:23px;width:8px;height:8px;border-radius:50%;background:var(--white)}
.slide-dots span.on{background:var(--accent)}
.pager{position:absolute;left:0;top:650px;width:330px;height:60px;background:rgba(0,0,0,.6);font-size:11px}

/* about */
.about{position:absolute;left:0;top:710px;width:1200px;height:588px;background:var(--white);color:var(--body-text)}
.section-title{position:absolute;width:100%;text-align:center;font-size:32px;font-weight:400;color:#555}
.section-title b{font-weight:500;color:#1d1d1d}
.product-shot{position:absolute;top:139px;width:352px;height:353px;background:radial-gradient(ellipse at 50% 45%,#2a2c55 0%,#171a33 45%,#0b0c14 100%);box-shadow:4px 6px 10px rgba(0,0,0,.35)}
.about-text{position:absolute;left:801px;top:138px;width:365px}
.about-text h3{font-size:26px;line-height:32px;font-weight:400;color:#111;margin-bottom:12px}
.about-text p{font-size:12.5px;line-height:17px;font-weight:500;color:#444;margin-bottom:18px;text-align:justify}

/* feature columns */
.features{position:absolute;left:0;top:1298px;width:1200px;height:747px;display:flex}
.feature{position:relative;width:300px;height:747px;overflow:hidden}
.feature .photo{position:absolute;inset:0}
.feature .shade{position:absolute;inset:0;background:rgba(0,0,0,.72)}
.feature h4{position:absolute;left:50px;top:92px;font-size:22px;line-height:29px;font-weight:500;letter-spacing:.5px}
.feature .side{position:absolute;left:47px;bottom:72px;writing-mode:vertical-rl;transform:rotate(180deg);font-size:22px;font-weight:400;letter-spacing:.5px}
.view-badge{position:absolute;left:703px;top:1611px;width:74px;height:74px;border-radius:50%;background:var(--accent-deep);display:flex;align-items:center;justify-content:center}

/* clients */
.clients{position:absolute;left:0;top:2045px;width:1200px;height:790px;background:var(--charcoal)}
.clients-title{position:absolute;left:0;width:100%;top:118px;text-align:center;font-family:"Archivo Black",Arial,sans-serif;font-size:100px;line-height:120px;letter-spacing:2px;background:linear-gradient(90deg,#8a6a50 0%,#4a3a30 25%,#b0794f 50%,#5c4b40 70%,#c0844f 100%);-webkit-background-clip:text;background-clip:text;color:transparent}
.divider{position:absolute;top:255px;width:3px;height:346px;background:#d9d9d9}
.hex{position:absolute;width:118px;height:104px}
.hex span{position:absolute;inset:0;display:flex;align-items:center;justify-content:center;text-align:center;font-size:24px;line-height:30px;font-weight:700;color:var(--hex-text)}

/* contact */
.contact{position:absolute;left:0;top:2835px;width:1200px;height:581px;overflow:hidden}
.contact .photo{position:absolute;inset:0;background:radial-gradient(ellipse at 75% 40%,#5a3a30 0%,#3a2620 40%,#1a1210 100%)}
.contact .shade{position:absolute;inset:0;background:rgba(0,0,0,.5)}
.contact h2{position:absolute;width:100%;top:30px;text-align:center;font-size:40px;font-weight:500}
.contact h2 em{font-style:normal;color:var(--gold)}
.field{position:absolute;background:rgba(58,59,61,.92);font-size:12px;padding:14px 12px;color:var(--muted)}
.info{position:absolute;left:811px;font-size:16px;line-height:22px;font-weight:500}
.info-line{position:absolute;left:800px;top:3073px;width:352px;height:2px;background:var(--white)}
.footer-logo{position:absolute;left:46px;top:3362px;font-size:27px;font-weight:400}
.footer-nav{position:absolute;left:371px;top:3375px;font-size:14px;display:flex}
.footer-nav a{color:var(--white);text-decoration:none}
.footer-nav i{font-style:normal;margin:0 8px}
.copyright{position:absolute;right:48px;top:3375px;font-size:14px}
.copyright em{font-style:normal;color:var(--accent-deep)}
</style>
</head>
<body>

<header class="hero">
  <div class="hero-photo" role="img" aria-label="Modern glass and concrete office building with trees in front"></div>
  <div class="hero-shade"></div>
  <div class="hero-topband"></div>
  <div class="hero-rail"></div>
  <div class="hero-rail-line"></div>
  <div class="social" style="top:291px"></div>
  <div class="social" style="top:328px"></div>
  <div class="social" style="top:365px"></div>
  <div class="social" style="top:402px"></div>
  <div class="social" style="top:439px"></div>
  <div class="social" style="top:476px"></div>

  <div class="brand-box">
    <div class="name">LOGO<br>HERE</div>
    <div class="count">-06</div>
    <div class="index">02</div>
  </div>

  <nav class="main-nav">
    <span style="left:373px">+192-34-23</span>
    <a href="#" style="left:585px">HOME</a>
    <a href="#" style="left:669px">PRODUCTS</a>
    <a href="#" style="left:795px">ABOUT</a>
    <a href="#" style="left:888px">SERVICES</a>
    <a href="#" style="left:1000px">FAQ</a>
    <a href="#" style="left:1068px">CONTACT</a>
  </nav>

  <h1 class="hero-title">SAMPLE TITLE HERE</h1>
  <p class="hero-copy">Lorem ipsum dolor sit amet, consectetur adipisicing elit. Eveniet, odit illo. Quibusdam natus voluptas adipisci delectus pariatur quia dolor quasi.</p>
  <div class="btn" style="left:801px;top:464px;width:165px;height:37px">READ MORE</div>

  <div class="slide-dots">
    <span style="top:30px"></span><span style="top:50px"></span><span class="on" style="top:70px"></span><span style="top:90px"></span><span style="top:110px"></span>
  </div>
  <div class="pager">
    <svg class="abs" style="left:58px;top:22px" width="90" height="16" viewBox="0 0 90 16"><path d="M2 8H40M2 8l7-6M2 8l7 6" stroke="#fff" stroke-width="2" fill="none"/><text x="44" y="12" fill="#fff" font-size="11" font-family="Poppins,sans-serif">PREV</text></svg>
    <svg class="abs" style="left:196px;top:22px" width="80" height="16" viewBox="0 0 80 16"><text x="2" y="12" fill="#fff" font-size="11" font-family="Poppins,sans-serif">NEXT</text><path d="M36 8H76M76 8l-7-6M76 8l-7 6" stroke="#fff" stroke-width="2" fill="none"/></svg>
  </div>
</header>

<section class="about">
  <h2 class="section-title" style="top:52px">ABOUT <b>LOGO HERE</b></h2>
  <div class="product-shot" style="left:48px" role="img" aria-label="Back of a dark blue smartphone"></div>
  <div class="product-shot" style="left:424px" role="img" aria-label="Back of a dark blue smartphone at an angle"></div>
  <div class="about-text">
    <h3>SAMPLE TEXT HERE</h3>
    <p>Lorem ipsum dolor sit amet, consectetur<br>adipisicing elit. Reiciendis provident, ab et voluptas quae minus recusandae aepe eum amet ex. Animi eligendi, hic non distinctio ad quaerat maiores, excepturi illo.</p>
    <p>Lorem ipsum dolor sit amet, consectetur<br>adipisicing elit. Reiciendis provident, ab et voluptas quae minus recusandae aepe eum amet ex. Animi eligendi, hic non distinctio ad quaerat maiores, excepturi illo.</p>
    <p>Lorem ipsum dolor sit amet, consectetur<br>adipisicing elit. Reiciendis provident, ab et voluptas quae minus recusandae aepe eum amet ex. Animi eligendi, hic non distinctio ad quaerat maiores, excepturi illo.</p>
  </div>
</section>

<section class="features">
  <article class="feature">
    <div class="photo" role="img" aria-label="Canvas sneakers on autumn leaves" style="background:linear-gradient(160deg,#3a3f4a,#5a4236 60%,#6e3a24)"></div>
    <div class="shade"></div>
    <h4>SAMPLE TTITLE<br>TEXT HERE</h4>
    <div class="side">SAMPLE TEXT HERE</div>
  </article>
  <article class="feature">
    <div class="photo" role="img" aria-label="Person in a denim jacket" style="background:linear-gradient(170deg,#4a4440,#5b4a3e 50%,#6a4a32)"></div>
    <div class="shade"></div>
    <h4>SAMPLE TTITLE<br>TEXT HERE</h4>
    <div class="side">SAMPLE TEXT HERE</div>
  </article>
  <article class="feature">
    <div class="photo" role="img" aria-label="Close-up of a flag-patterned sneaker on autumn leaves" style="background:linear-gradient(180deg,#2e3a5c 0%,#7a4a52 35%,#b0484a 55%,#4a4f6a 75%,#8a4a2a 100%)"></div>
  </article>
  <article class="feature">
    <div class="photo" role="img" aria-label="Person in a striped sweater" style="background:linear-gradient(170deg,#6a4a3a,#7a3a30 50%,#3a3a40)"></div>
    <div class="shade" style="background:rgba(0,0,0,.66)"></div>
    <h4>SAMPLE TTITLE<br>TEXT HERE</h4>
    <div class="side">SAMPLE TEXT HERE</div>
  </article>
</section>
<div class="view-badge">
  <svg width="44" height="30" viewBox="0 0 44 30"><path d="M2 15C10 3 34 3 42 15C34 27 10 27 2 15Z" fill="#fff"/><circle cx="22" cy="15" r="8" fill="#f0a23c"/><circle cx="22" cy="15" r="4" fill="#fff"/></svg>
</div>

<section class="clients">
  <div class="clients-title">OUR CLIENTS</div>
  <div class="divider" style="left:222px"></div>
  <div class="divider" style="left:411px"></div>
  <div class="divider" style="left:598px"></div>
  <div class="divider" style="left:787px"></div>
  <div class="divider" style="left:976px"></div>

  <div class="hex" style="left:71px;top:346px"><svg width="118" height="104"><polygon points="30,0 88,0 118,52 88,104 30,104 0,52" fill="#6d6d6d"/></svg><span>LOGO<br>HERE</span></div>
  <div class="hex" style="left:260px;top:346px"><svg width="118" height="104"><polygon points="30,0 88,0 118,52 88,104 30,104 0,52" fill="#6d6d6d"/></svg><span>LOGO<br>HERE</span></div>
  <div class="hex" style="left:446px;top:346px"><svg width="118" height="104"><polygon points="30,0 88,0 118,52 88,104 30,104 0,52" fill="#6d6d6d"/></svg><span>LOGO<br>HERE</span></div>
  <div class="hex" style="left:635px;top:346px"><svg width="118" height="104"><polygon points="30,0 88,0 118,52 88,104 30,104 0,52" fill="#6d6d6d"/></svg><span>LOGO<br>HERE</span></div>
  <div class="hex" style="left:824px;top:346px"><svg width="118" height="104"><polygon points="30,0 88,0 118,52 88,104 30,104 0,52" fill="#6d6d6d"/></svg><span>LOGO<br>HERE</span></div>
  <div class="hex" style="left:1011px;top:346px"><svg width="118" height="104"><polygon points="30,0 88,0 118,52 88,104 30,104 0,52" fill="#6d6d6d"/></svg><span>LOGO<br>HERE</span></div>

  <div class="hex" style="left:71px;top:510px"><svg width="118" height="104"><polygon points="30,0 88,0 118,52 88,104 30,104 0,52" fill="#6d6d6d"/></svg><span>LOGO<br>HERE</span></div>
  <div class="hex" style="left:260px;top:510px"><svg width="118" height="104"><polygon points="30,0 88,0 118,52 88,104 30,104 0,52" fill="#6d6d6d"/></svg><span>LOGO<br>HERE</span></div>
  <div class="hex" style="left:446px;top:510px"><svg width="118" height="104"><polygon points="30,0 88,0 118,52 88,104 30,104 0,52" fill="#6d6d6d"/></svg><span>LOGO<br>HERE</span></div>
  <div class="hex" style="left:635px;top:510px"><svg width="118" height="104"><polygon points="30,0 88,0 118,52 88,104 30,104 0,52" fill="#6d6d6d"/></svg><span>LOGO<br>HERE</span></div>
  <div class="hex" style="left:824px;top:510px"><svg width="118" height="104"><polygon points="30,0 88,0 118,52 88,104 30,104 0,52" fill="#6d6d6d"/></svg><span>LOGO<br>HERE</span></div>
  <div class="hex" style="left:1011px;top:510px"><svg width="118" height="104"><polygon points="30,0 88,0 118,52 88,104 30,104 0,52" fill="#6d6d6d"/></svg><span>LOGO<br>HERE</span></div>
</section>

<section class="contact">
  <div class="photo" role="img" aria-label="Flag-patterned sneakers on autumn leaves, blurred"></div>
  <div class="shade"></div>
  <h2>GET IN <em>TOUCH</em></h2>
</section>
<div class="field" style="left:48px;top:2958px;width:186px;height:48px">Name:</div>
<div class="field" style="left:246px;top:2958px;width:187px;height:48px">Address</div>
<div class="field" style="left:48px;top:3028px;width:186px;height:48px">Email:</div>
<div class="field" style="left:246px;top:3028px;width:187px;height:48px">Phone</div>
<div class="field" style="left:444px;top:2958px;width:371px;height:118px">Message</div>
<div class="btn" style="left:48px;top:3101px;width:186px;height:37px;color:#222">SEND</div>
<div class="info" style="top:2965px">+194-34-23</div>
<div class="info" style="top:2999px">sample@email.com</div>
<div class="info" style="top:3033px">123 Block 1, Sample Address Here</div>
<div class="info-line"></div>

<footer>
  <div class="footer-logo">LOGO HERE</div>
  <nav class="footer-nav"><a href="#">HOME</a><i>|</i><a href="#">PRODUCTS</a><i>|</i><a href="#">ABOUT</a><i>|</i><a href="#">SERVICES</a><i>|</i><a href="#">FAQ</a></nav>
  <div class="copyright">Copyright 2018 | <em>Company Name</em></div>
</footer>

</body>
</html>
```